Postcard Design for Marketing to Builders

I am an architect that gets most of my work from contractor's. I design residential and commercial projects based in California. My main focus is California's Central Coast. I want the feel of the postcard to reflect a strong professional, efficient and creative partner for contractors (Builders). I have provide some photos of projects I have done recently to use on the postcard if needed. I have also included my logo which I would like on the front.

Industry/Entity Type

Architect

Font styles to use
Serif

```html
<!DOCTYPE html>
<html lang="en">
<head>
<meta charset="utf-8">
<title>Daniel R Harlow Architect – Builder Postcard</title>
<link rel="stylesheet" href="https://fonts.googleapis.com/css2?family=Lato:wght@400;700;900&family=Roboto+Condensed:wght@700&display=swap">
<style>
  :root {
    --navy: #26296b;
    --orange: #f47b20;
    --white: #ffffff;
    --panel-light: #ffffff;
    --panel-grey: #d9d9db;
    --ink: #1e1f3a;
    --stage: #e4e4e6;
    --sky: #6f9fd8;
    --sky-light: #c9dcf0;
    --facade: #eee6cf;
    --lawn: #6c9a45;
  }
  * { box-sizing: border-box; margin: 0; padding: 0; }
  html, body { width: 916px; height: 1200px; overflow: hidden; }
  body { background: var(--stage); position: relative; font-family: 'Lato', sans-serif; }

  .postcard { position: absolute; left: 41px; width: 834px; background: var(--white); overflow: hidden; }
  .postcard--front { top: 43px; height: 538px; }
  .postcard--back { top: 613px; height: 542px; }
  .postcard svg.artwork { position: absolute; inset: 0; width: 100%; height: 100%; display: block; }

  .brand-name {
    position: absolute; left: 24px; top: 70px; width: 190px;
    font-family: 'Lato', sans-serif; font-weight: 700; font-size: 19px;
    line-height: 1.15; letter-spacing: 0.04em; text-transform: uppercase;
    color: var(--navy); text-align: center;
  }

  .call-to-action {
    position: absolute; left: 0; right: 0; top: 460px; text-align: center;
    font-family: 'Lato', sans-serif; font-weight: 700; font-size: 49px; letter-spacing: -0.01em;
  }
  .call-to-action .label { color: var(--orange); margin-right: 10px; }
  .call-to-action .number { color: var(--white); }

  .tab-label {
    position: absolute; left: 20px;
    font-family: 'Roboto Condensed', sans-serif; font-weight: 700; font-size: 17px;
    color: var(--ink); text-transform: uppercase; letter-spacing: 0.01em; line-height: 26px;
  }
  .tab-label--service { top: 29px; }
  .tab-label--specialty { top: 125px; }

  .service-area { position: absolute; left: 21px; top: 68px; font-size: 23px; font-weight: 400; color: var(--ink); }

  .specialty-list { position: absolute; left: 20px; top: 162px; list-style: none; font-size: 13.5px; color: var(--ink); line-height: 16.5px; }
  .specialty-list li::before { content: "•"; margin-right: 4px; }

  .contact-list { position: absolute; left: 14px; top: 468px; list-style: none; color: var(--white); font-size: 13px; line-height: 16px; }
  .contact-list li { display: flex; align-items: flex-start; gap: 6px; margin-bottom: 6px; }
  .contact-list svg { flex: none; width: 13px; height: 14px; margin-top: 1px; }

  .stamp-box { position: absolute; left: 754px; top: 35px; width: 50px; height: 68px; border: 1px solid #555; }
</style>
</head>
<body>

<section class="postcard postcard--front" aria-label="Postcard front">
  <svg class="artwork" viewBox="0 0 834 538" aria-hidden="false">
    <defs>
      <linearGradient id="front-panel" x1="0" y1="0" x2="1" y2="0">
        <stop offset="0" stop-color="var(--panel-grey)"/>
        <stop offset="0.55" stop-color="var(--panel-light)"/>
      </linearGradient>
      <linearGradient id="hero-tones" x1="0" y1="0" x2="0" y2="1">
        <stop offset="0" stop-color="var(--sky)"/>
        <stop offset="0.35" stop-color="var(--sky-light)"/>
        <stop offset="0.55" stop-color="var(--facade)"/>
        <stop offset="0.8" stop-color="var(--lawn)"/>
        <stop offset="1" stop-color="#8c8f93"/>
      </linearGradient>
      <linearGradient id="timber-tones" x1="0" y1="0" x2="0" y2="1">
        <stop offset="0" stop-color="#dfe8ef"/>
        <stop offset="0.45" stop-color="#a4643a"/>
        <stop offset="1" stop-color="#4b2e1c"/>
      </linearGradient>
      <linearGradient id="glass-tones" x1="0" y1="0" x2="0" y2="1">
        <stop offset="0" stop-color="#9fc1e4"/>
        <stop offset="0.5" stop-color="#5d6a72"/>
        <stop offset="1" stop-color="#c9b79a"/>
      </linearGradient>
    </defs>

    <rect class="front-panel" width="834" height="538" fill="url(#front-panel)"/>

    <path class="accent-swoosh accent-swoosh--orange" d="M429 0 C368 80 368 220 448 300 C488 340 528 380 546 420 L834 420 L834 0 Z" fill="var(--orange)"/>
    <path class="accent-swoosh accent-swoosh--navy" d="M446 0 C385 80 385 220 465 300 C505 340 545 380 563 420 L834 420 L834 0 Z" fill="var(--navy)"/>
    <path class="accent-swoosh accent-swoosh--gap" d="M455 0 C394 80 394 220 474 300 C514 340 554 380 572 420 L834 420 L834 0 Z" fill="var(--white)"/>
    <g role="img" aria-label="Photo of a completed single-storey clubhouse with white gabled entry, glass doors and landscaped lawn">
      <path class="hero-photo" d="M461 0 C400 80 400 220 480 300 C520 340 560 380 578 420 L834 420 L834 0 Z" fill="url(#hero-tones)"/>
    </g>

    <path class="band-rule" d="M0 460 Q420 356 834 452" fill="none" stroke="var(--orange)" stroke-width="5"/>
    <path class="cta-band" d="M0 472 Q420 368 834 464 L834 538 L0 538 Z" fill="var(--navy)"/>

    <g class="project-thumb">
      <circle cx="117" cy="270" r="86" fill="var(--orange)"/>
      <circle cx="117" cy="270" r="80" fill="var(--white)"/>
      <circle cx="117" cy="270" r="76" fill="url(#timber-tones)" role="img" aria-label="Photo of a timber-framed gabled entry porch"/>
    </g>
    <g class="project-thumb">
      <circle cx="333" cy="336" r="86" fill="var(--orange)"/>
      <circle cx="333" cy="336" r="80" fill="var(--white)"/>
      <circle cx="333" cy="336" r="76" fill="url(#glass-tones)" role="img" aria-label="Photo of a glass-walled building with a paved patio"/>
    </g>
  </svg>

  <div class="brand-name">Daniel R Harlow<br>Architect</div>

  <p class="call-to-action"><span class="label">Call now</span><span class="number">805-555-0142</span></p>
</section>

<section class="postcard postcard--back" aria-label="Postcard back">
  <svg class="artwork" viewBox="0 0 834 542" aria-hidden="true">
    <defs>
      <linearGradient id="back-panel" x1="0" y1="0" x2="1" y2="0">
        <stop offset="0" stop-color="var(--panel-grey)"/>
        <stop offset="0.5" stop-color="var(--panel-light)"/>
        <stop offset="1" stop-color="var(--panel-grey)"/>
      </linearGradient>
    </defs>
    <rect class="info-panel" width="362" height="542" fill="url(#back-panel)"/>
    <path class="label-tab" d="M0 29 H133 A13 13 0 0 1 133 55 H0 Z" fill="var(--orange)"/>
    <path class="label-tab" d="M0 125 H133 A13 13 0 0 1 133 151 H0 Z" fill="var(--orange)"/>
    <path class="band-rule" d="M0 436 Q181 394 362 434" fill="none" stroke="var(--orange)" stroke-width="4"/>
    <path class="contact-band" d="M0 446 Q181 404 362 444 L362 542 L0 542 Z" fill="var(--navy)"/>
  </svg>

  <span class="tab-label tab-label--service">Service Area</span>
  <p class="service-area">Central Coast</p>

  <span class="tab-label tab-label--specialty">Specializing</span>
  <ul class="specialty-list">
    <li>Custom Residences</li>
    <li>Commercial</li>
    <li>Tenant Improvement</li>
    <li>Residential Remodels</li>
  </ul>

  <ul class="contact-list">
    <li>
      <svg viewBox="0 0 24 24" aria-hidden="true"><path fill="var(--orange)" d="M6.6 10.8a15.1 15.1 0 0 0 6.6 6.6l2.2-2.2a1 1 0 0 1 1-.25 11.4 11.4 0 0 0 3.6.57 1 1 0 0 1 1 1V20a1 1 0 0 1-1 1A17 17 0 0 1 3 4a1 1 0 0 1 1-1h3.5a1 1 0 0 1 1 1c0 1.25.2 2.45.57 3.57a1 1 0 0 1-.25 1z"/></svg>
      <span>805-555-0142</span>
    </li>
    <li>
      <svg viewBox="0 0 24 24" aria-hidden="true"><path fill="var(--orange)" d="M12 2a7 7 0 0 0-7 7c0 5.2 7 13 7 13s7-7.8 7-13a7 7 0 0 0-7-7zm0 9.5A2.5 2.5 0 1 1 12 6.5a2.5 2.5 0 0 1 0 5z"/></svg>
      <span>PO Box 4820,<br>Arroyo Vista, CA 93420</span>
    </li>
  </ul>

  <div class="stamp-box" aria-label="Stamp area"></div>
</section>

</body>
</html>
```